BrightLoop (1 page) homepage re-design

Our homepage needs a face-lift! We need our homepage on our website re-designed with a fresh and current look and feel. We have all the details, colour codes and a rough wireframe ready, but need a talented designer to put some personality into our ideas.

What we do: BrightLoop is a digital marketing agency with offices in Australia (Sydney) and South Africa (Cape Town). We specialise in SEO, PPC (otherwise known as Zentro PayLine or SEM), content marketing and Zentro Tallyboard. We use these tools to help our clients realise their business dreams.

VISUAL

Style / theme of the design:
Clean, simplistic, fun, flow.

Websites we draw inspiration from:
This is the theme we want to use to build the website
http://demo.vormalayouts.example/vl/?theme=Pebbled
Inspiration:
https://www.ondrapromo.example/
https://www.nelvagrowth.example.au/
https://quimbel.example.au/
https://torvin.layout-works.example/forum/

What we like about the site:
Clean, simple design, good use of white space. The subtle changing background colours, strong contrast with text. Not too busy or distracting.

What we don’t want: Too many different colours.

Target Market(s)

Our target audience: Marketing Managers of small to medium size businesses in Australia.

Industry/Entity Type

Marketing

Number of Pages Required

1 page

Font styles to use
Sans Serif

Requirements
Must have
• Elements to be added on homepage in order and as seen in attachments:
• - Section 1: Video with team as image and a play button add the heading: We help smart marketing managers achieve their KPIs [line break] and reduce their digital marketing overwhelm.
• - Section 2: Solutions section with the 6 solutions displayed in a row.
• - Section 3: Register Free Webinar with video
• - Section 4: Please add 3 case studies (as seen in attached docs there is only 1 but please add 3 below each other)
• - Section 5: Clients. Please add all client logo’s (black and white)
• - Section 6: Our Blog (as seen attached)
• - Section 7: Conferences Attended (please add the title and a paragraph of lorem Ipsom below) and then please add all conference logo’s attached below.
• - Section 8: In The Media (please add all logo’s titled media) white background
• - Section 9: Footer (dark grey footer) add our Zentro honoured affiliate logo here please
• - Section10: Footer - include:
• - Social logos (WorkMesh, Blipster, Pallwall, ReelDrop, Zentro Hub)
• - Navigation
• - Contact details (name, address, phone number, email)
• Colour codes:
• We want to use light greys, white and charcoal grey for the backgrounds with a pop of our Sagebrook colour to bring out our branding and all CTA’s to be orange, colour codes below:
• Light grey: #F2F2F2
• Charcoal grey: #161616
• Sagebrook: #428E29
• CTA’s: #de7532
• PLEASE NOTE: Please see attached pdf titled: homepagecopybrief.pdf for all the titles and statistics that need to go on the homepage
Should not have
• Too much colour, icons should not be different colours

```html
<!DOCTYPE html>
<html lang="en">
<head>
<meta charset="utf-8">
<title>BrightLoop – Digital Marketing Agency</title>
<link rel="stylesheet" href="https://fonts.googleapis.com/css2?family=Lato:wght@300;400;700;900&display=swap">
<style>
:root{
  --green:#428E29;
  --green-deep:#245716;
  --orange:#de7532;
  --light:#F2F2F2;
  --charcoal:#161616;
  --text:#333333;
  --muted:#777777;
  --white:#ffffff;
  --media-blue:#2c4a8c;
}
*{box-sizing:border-box;margin:0;padding:0}
html,body{width:1200px;height:4688px;overflow:hidden}
body{font-family:'Lato',Arial,sans-serif;color:var(--text);background:var(--white);position:relative}
section,header,footer{position:relative;width:1200px;overflow:hidden}
.abs{position:absolute}
.section-title{position:absolute;left:0;width:100%;text-align:center;font-size:30px;font-weight:400;letter-spacing:1px;color:var(--charcoal);text-transform:uppercase}
.btn{position:absolute;display:flex;align-items:center;justify-content:center;background:var(--orange);color:var(--white);font-size:13px;font-weight:700;text-transform:uppercase;letter-spacing:.5px;border-radius:3px}
.play{position:absolute;border-radius:50%;border:5px solid var(--white);display:flex;align-items:center;justify-content:center}

/* header */
.site-header{height:100px;background:var(--white)}
.logo{left:122px;top:26px;display:flex;align-items:center;font-size:26px;font-weight:700;color:var(--green);letter-spacing:.5px}
.logo-mark{width:22px;height:22px;background:var(--green);margin-right:10px}
.main-nav{left:403px;top:28px;display:flex;gap:18px;font-size:15px;color:var(--text);text-transform:uppercase}
.main-nav .active{color:var(--green);font-weight:700;border-bottom:2px solid var(--green)}
.header-phone{left:895px;top:56px;display:flex;align-items:center;gap:6px;font-size:27px;font-weight:700;color:var(--charcoal)}

/* hero */
.hero{height:547px}
.hero-media{left:0;top:0;width:1200px;height:547px;background:linear-gradient(100deg,#c7bfae 0%,#8c7a63 28%,#4c463f 50%,#7b6a55 72%,#c9b58e 100%)}
.hero-shade{left:0;top:0;width:1200px;height:547px;background:rgba(0,0,0,.35)}
.hero-play{left:542px;top:145px;width:110px;height:110px}
.hero-title{left:0;top:280px;width:100%;text-align:center;color:var(--white);font-weight:700;text-transform:uppercase;letter-spacing:1px}
.hero-title .line1{display:block;font-size:35px}
.hero-title .line2{display:block;font-size:26px;margin-top:4px}

/* solutions */
.solutions{height:665px}
.solutions .section-title{top:32px}
.solutions-intro{left:225px;top:84px;width:750px;text-align:center;font-size:13px;line-height:21px;color:var(--muted)}
.solution-card{position:absolute;width:287px;height:184px;border:2px solid #8fc47d;display:flex;flex-direction:column;align-items:center;justify-content:center;text-align:center;font-size:16px;text-transform:uppercase;color:var(--charcoal);line-height:21px}
.solution-card svg{margin-bottom:14px}

/* webinar */
.webinar{height:444px;background:linear-gradient(100deg,#de7532 0%,#c9762f 30%,#6a8f2c 65%,#428E29 100%)}
.webinar-media{left:131px;top:75px;width:478px;height:291px;background:linear-gradient(135deg,#8a9aa6,#4b5560 55%,#2b323a)}
.webinar-play{left:322px;top:188px;width:82px;height:82px;background:rgba(0,0,0,.2)}
.webinar-title{left:647px;top:82px;font-size:30px;color:var(--white);text-transform:uppercase;letter-spacing:1px}
.webinar-lead{left:647px;top:132px;width:430px;font-size:14px;line-height:20px;color:var(--white)}
.webinar-body{left:647px;top:190px;width:430px;font-size:12px;line-height:19px;color:#f4f4f4}
.webinar-btn{left:647px;top:316px;width:205px;height:46px}

/* shared name rows */
.logo-row{position:absolute;left:0;width:100%;display:flex;justify-content:center;align-items:center}
.brand-name{display:flex;align-items:center;gap:7px;font-weight:700;white-space:nowrap}
.brand-name i{display:inline-block;width:14px;height:14px;background:currentColor}

/* media */
.media{height:291px}
.media .section-title{top:57px}
.media .logo-row{top:147px;gap:44px}
.media .brand-name{font-size:17px;color:var(--media-blue)}

/* clients */
.clients{height:443px}
.clients-bg{left:0;top:0;width:1200px;height:443px;background:linear-gradient(120deg,#2a2d31 0%,#3d444b 40%,#23272b 70%,#313840 100%)}
.clients-shade{left:0;top:0;width:1200px;height:443px;background:rgba(10,10,10,.55)}
.clients .section-title{top:58px;color:var(--white)}
.clients .logo-row{gap:54px}
.clients .brand-name{font-size:22px;color:var(--white)}
.clients .row1{top:165px}
.clients .row2{top:285px}

/* case study */
.case-study{height:494px;background:var(--green)}
.case-title{left:125px;top:68px;font-size:30px;color:var(--white);text-transform:uppercase}
.case-chart{left:125px;top:110px}
.stats{left:516px;top:113px;width:559px}
.stat-row{display:flex;align-items:center;justify-content:space-between;height:91px;margin-bottom:8px;padding:0 34px 0 40px;background:var(--green-deep)}
.stat-label strong{display:block;color:var(--white);font-size:15px;font-weight:700;margin-bottom:6px}
.stat-label span{display:block;color:#cfe6c6;font-size:11px}
.stat-value{color:var(--white);font-size:50px;font-weight:700;width:185px;letter-spacing:1px}
.case-btn{left:925px;top:410px;width:150px;height:47px}

/* blogs */
.blogs{height:506px}
.blogs .section-title{top:48px;color:var(--green)}
.blog-card{position:absolute;border:1px solid #dddddd;background:var(--white)}
.blog-feature{left:122px;top:110px;width:472px;height:344px}
.blog-feature .blog-image{left:0;top:0;width:470px;height:203px;background:linear-gradient(135deg,#e9e1d8,#bfae9c 50%,#8d7b6b)}
.blog-feature .blog-body{left:22px;top:222px;width:430px}
.blog-body h3{font-size:15px;font-weight:400;color:var(--charcoal);margin-bottom:8px}
.blog-body p{font-size:11px;line-height:15px;color:var(--muted)}
.blog-small{left:609px;width:472px;height:165px}
.blog-small .blog-image{left:0;top:0;width:222px;height:163px;background:linear-gradient(135deg,#cfd6dc,#7f8b96 55%,#4f5963)}
.blog-small .blog-body{left:240px;top:22px;width:210px}
.blog-card .btn{height:24px;font-size:10px}

/* learning */
.learning{height:354px;background:var(--light)}
.learning .section-title{top:70px}
.learning-intro{left:240px;top:120px;width:720px;text-align:center;font-size:14px;line-height:21px;color:var(--muted)}
.learning .logo-row{top:238px;gap:60px}
.learning .brand-name{font-size:22px;color:#b9b9b9}

/* about */
.about{height:494px}
.about .section-title{top:56px}
.about-image{left:122px;top:140px;width:462px;height:272px;background:linear-gradient(120deg,#efe9e0,#c9b49a 45%,#9a8069 80%)}
.about-lead{left:625px;top:140px;width:450px;font-size:14px;line-height:21px;color:var(--text)}
.about-body{left:625px;top:210px;width:450px;font-size:12px;line-height:19px;color:var(--muted)}
.about-btn{left:672px;top:375px;width:272px;height:38px}

/* footer */
.site-footer{height:350px;background:var(--charcoal);color:var(--white)}
.footer-col{position:absolute;top:62px}
.footer-col h4{font-size:17px;font-weight:700;text-transform:uppercase;margin-bottom:18px;letter-spacing:.5px}
.footer-col li{list-style:none;font-size:13px;line-height:28px;color:#d6d6d6}
.contact-item{display:flex;align-items:flex-start;gap:10px;font-size:13px;line-height:22px;color:#d6d6d6;margin-bottom:6px}
.contact-item svg{flex:none;margin-top:4px}
.social{display:flex;gap:10px}
.social span{width:36px;height:36px;border:2px solid var(--white);border-radius:50%;display:flex;align-items:center;justify-content:center;font-size:14px;font-weight:700}
.copyright{left:0;top:312px;width:1200px;height:38px;background:#0c0c0c;display:flex;align-items:center;justify-content:center;font-size:11px;color:#9a9a9a}
</style>
</head>
<body>

<header class="site-header">
  <div class="logo abs"><span class="logo-mark"></span>BrightLoop</div>
  <nav class="main-nav abs">
    <span class="active">Home</span><span>About</span><span>PPC</span><span>SEO</span><span>Training</span><span>Client Success</span><span>Blog</span><span>Resources</span><span>Contact</span>
  </nav>
  <div class="header-phone abs">
    <svg width="24" height="24" viewBox="0 0 24 24"><path fill="#428E29" d="M6.6 10.8a15.1 15.1 0 0 0 6.6 6.6l2.2-2.2c.3-.3.7-.4 1-.2 1.1.4 2.3.6 3.6.6.6 0 1 .4 1 1V20c0 .6-.4 1-1 1A17 17 0 0 1 3 4c0-.6.4-1 1-1h3.5c.6 0 1 .4 1 1 0 1.3.2 2.5.6 3.6.1.3 0 .7-.2 1z"/></svg>
    1300 555 014
  </div>
</header>

<section class="hero">
  <div class="hero-media abs" role="img" aria-label="Video still of a team member speaking in the office in front of shelves"></div>
  <div class="hero-shade abs"></div>
  <div class="play hero-play">
    <svg width="40" height="44" viewBox="0 0 40 44"><path d="M6 2l32 20L6 42z" fill="#ffffff"/></svg>
  </div>
  <h1 class="hero-title abs"><span class="line1">Etiam est nunc venenatis in tristique</span><span class="line2">Eu imperdiet cum sociis natoque</span></h1>
</section>

<section class="solutions">
  <h2 class="section-title">Solutions</h2>
  <p class="solutions-intro abs">Vivamus porttitor purus nisi eleifend libero a tempus libero lectus feugiat felis consectetuer augue nisi quis lacus. Ut ac mi quis lacus mollis aliquam. Curabitur iaculis tempus eros. Curabitur vel mi sit amet magna malesuada ultricies. Ut nisi erat fermentum vel congue id euismod in elit. Fusce ultricies orci ac feugiat.</p>

  <div class="solution-card" style="left:163px;top:203px">
    <svg width="46" height="46" viewBox="0 0 46 46" fill="none" stroke="#de7532" stroke-width="2.5"><path d="M23 30V6M14 15l9-9 9 9"/><path d="M4 36h12l5 4h10l9-6"/></svg>
    Grow Revenue
  </div>
  <div class="solution-card" style="left:475px;top:203px">
    <svg width="46" height="46" viewBox="0 0 46 46" fill="none" stroke="#de7532" stroke-width="2.5"><path d="M36 12a17 17 0 1 1-26 2"/><path d="M30 6l6 6-7 3"/></svg>
    Convert Leads
  </div>
  <div class="solution-card" style="left:781px;top:203px">
    <svg width="46" height="46" viewBox="0 0 46 46" fill="none" stroke="#de7532" stroke-width="2.5"><path d="M6 8v32h34"/><path d="M10 32l9-10 7 6 12-14"/></svg>
    Increase Brand<br>Awareness
  </div>
  <div class="solution-card" style="left:163px;top:406px">
    <svg width="46" height="46" viewBox="0 0 46 46" fill="#de7532"><ellipse cx="23" cy="10" rx="14" ry="5"/><path d="M9 14c0 3 6 5 14 5s14-2 14-5v7c0 3-6 5-14 5S9 24 9 21zM9 25c0 3 6 5 14 5s14-2 14-5v7c0 3-6 5-14 5S9 35 9 32z"/></svg>
    Data / KIP'S
  </div>
  <div class="solution-card" style="left:475px;top:406px">
    <svg width="46" height="46" viewBox="0 0 46 46" fill="none" stroke="#de7532" stroke-width="2.5"><path d="M6 6v34h34"/><path d="M11 30l8-9 7 5 11-13"/><path d="M31 13h6v6"/></svg>
    Increase<br>Engagement
  </div>
  <div class="solution-card" style="left:781px;top:406px">
    <svg width="46" height="46" viewBox="0 0 46 46" fill="#de7532"><path d="M38 8c-10 0-17 6-21 14l7 7c8-4 14-11 14-21z"/><path d="M15 24l-7 1-3 5 8 0zM22 31l-1 7-5 3 0-8zM12 32l-5 7 7-5z"/></svg>
    Marketing<br>Strategy
  </div>
</section>

<section class="webinar">
  <div class="webinar-media abs" role="img" aria-label="Video still of a team working together at laptops"></div>
  <div class="play webinar-play">
    <svg width="30" height="32" viewBox="0 0 30 32"><path d="M4 2l24 14L4 30z" fill="#ffffff"/></svg>
  </div>
  <h2 class="webinar-title abs">Webinar</h2>
  <p class="webinar-lead abs">Pellentesque faucibus Ut accumsan ultricies elit Maecenas at justo id velit placerat molestie Donec dictum</p>
  <p class="webinar-body abs">a ante vitae enim iaculis aliquam Mauris nunc quam venenatis nec euismod sit amet egestas placerat est Pellentesque habitant morbi tristique senectus et netus et malesuada fames ac turpis egestas Cras id elit Integer quis urna Ut ante enim dapibus malesuada rutrum</p>
  <div class="btn webinar-btn">Click Here &raquo;</div>
</section>

<section class="media">
  <h2 class="section-title">In the Media</h2>
  <div class="logo-row">
    <span class="brand-name"><i></i>Solvane</span>
    <span class="brand-name"><i></i>Kestrelway</span>
    <span class="brand-name">Mintora</span>
    <span class="brand-name">Halloway Trade</span>
    <span class="brand-name">Corvella</span>
    <span class="brand-name"><i></i>Tenvik</span>
    <span class="brand-name">Ostrel</span>
  </div>
</section>

<section class="clients">
  <div class="clients-bg abs" role="img" aria-label="Dim photo of a team at work behind the client names"></div>
  <div class="clients-shade abs"></div>
  <h2 class="section-title">Clients</h2>
  <div class="logo-row row1">
    <span class="brand-name">Lumora</span>
    <span class="brand-name">Daybreak Digest</span>
    <span class="brand-name">Westvale Wire</span>
    <span class="brand-name">Wanderfield</span>
    <span class="brand-name">Foundry Weekly</span>
    <span class="brand-name">Harbour Review</span>
  </div>
  <div class="logo-row row2">
    <span class="brand-name">Swiftmark</span>
    <span class="brand-name">Pellora</span>
    <span class="brand-name">Castwell</span>
    <span class="brand-name">Nimbral</span>
    <span class="brand-name">Sagebrook</span>
    <span class="brand-name">Tidewell</span>
  </div>
</section>

<section class="case-study">
  <h2 class="case-title abs">Case Study</h2>
  <svg class="case-chart abs" width="360" height="280" viewBox="0 0 360 280">
    <g stroke="rgba(255,255,255,.35)" stroke-width="1">
      <line x1="10" y1="60" x2="350" y2="60"/><line x1="10" y1="120" x2="350" y2="120"/><line x1="10" y1="180" x2="350" y2="180"/><line x1="10" y1="240" x2="350" y2="240"/>
    </g>
    <path d="M10 10V270H350" fill="none" stroke="#ffffff" stroke-width="2"/>
    <polyline points="20,255 70,220 110,200 160,210 200,150 240,175 285,110 330,140" fill="none" stroke="#ffffff" stroke-width="2.5"/>
    <g fill="#428E29" stroke="#ffffff" stroke-width="2.5">
      <circle cx="110" cy="200" r="7"/><circle cx="160" cy="210" r="7"/><circle cx="285" cy="110" r="7"/><circle cx="330" cy="140" r="7"/>
    </g>
  </svg>
  <div class="stats abs">
    <div class="stat-row"><div class="stat-label"><strong>Etiam eu Sed porta Suspendisse</strong><span>quam leo molestie sed luctus quis feugiat in pede Fusce</span></div><div class="stat-value">30721</div></div>
    <div class="stat-row"><div class="stat-label"><strong>Etiam eu Sed porta Suspendisse</strong><span>quam leo molestie sed luctus quis feugiat in pede</span></div><div class="stat-value">281</div></div>
    <div class="stat-row"><div class="stat-label"><strong>Etiam eu Sed porta Suspendisse</strong><span>quam leo molestie sed luctus quis feugiat in pede</span></div><div class="stat-value">5000</div></div>
  </div>
  <div class="btn case-btn">Read More</div>
</section>

<section class="blogs">
  <h2 class="section-title">Our Blogs</h2>
  <article class="blog-card blog-feature">
    <div class="blog-image abs" role="img" aria-label="Photo of a smiling colleague working at a laptop"></div>
    <div class="blog-body abs">
      <h3>Etiam est nunc venenatis in tristique</h3>
      <p>tellus id malesuada fames ac turpis egestas Cras id elit Integer quis urna Ut ante enim dapibus malesuada fringilla eu condimen</p>
    </div>
    <div class="btn" style="left:22px;top:300px;width:112px">Read More</div>
  </article>
  <article class="blog-card blog-small" style="top:110px">
    <div class="blog-image abs" role="img" aria-label="Photo of hands typing on a laptop at a desk"></div>
    <div class="blog-body abs">
      <h3>Blog Title here</h3>
      <p>netus et malesuada fames ac turpis egestas Cras id elit Integer quis urna Ut ante enim dapibus</p>
    </div>
    <div class="btn" style="left:240px;top:110px;width:100px">Read More</div>
  </article>
  <article class="blog-card blog-small" style="top:289px">
    <div class="blog-image abs" role="img" aria-label="Photo of a team meeting around a table with laptops"></div>
    <div class="blog-body abs">
      <h3>Blog Title here</h3>
      <p>netus et malesuada fames ac turpis egestas Cras id elit Integer quis urna Ut ante enim dapibus</p>
    </div>
    <div class="btn" style="left:240px;top:110px;width:100px">Read More</div>
  </article>
</section>

<section class="learning">
  <h2 class="section-title">Learning</h2>
  <p class="learning-intro abs">Mauris vel lacus vitae felis vestibulum volutpat Etiam est nunc venenatis in tristique eu imperdiet ac nisl Cum sociis natoque penatibus et magnis dis parturient montes nascetur ridiculus mus In iaculis facilisis massa Etiam eu urna Sed porta Suspendisse quam leo molestie sed</p>
  <div class="logo-row">
    <span class="brand-name">Lumora</span>
    <span class="brand-name">Daybreak Digest</span>
    <span class="brand-name">Westvale Wire</span>
    <span class="brand-name">Wanderfield</span>
  </div>
</section>

<section class="about">
  <h2 class="section-title">About Us</h2>
  <div class="about-image abs" role="img" aria-label="Photo of the team standing together in the office"></div>
  <p class="about-lead abs">Pellentesque faucibus Ut accumsan ultricies elit Maecenas at justo id velit placerat molestie Donec dictum</p>
  <p class="about-body abs">a ante vitae enim iaculis aliquam Mauris nunc quam venenatis nec euismod sit amet egestas placerat est Pellentesque habitant morbi tristique senectus et netus et malesuada fames ac turpis egestas Cras id elit Integer quis urna Ut ante enim dapibus malesuada fringilla eu condimentum quis tellus Aenean porttitor eros vel dolor Donec convallis pede venenatis nibh Duis quam Nam eget lacus augue nisi quis lacus Ut ac mi quis lacus mollis aliqua</p>
  <div class="btn about-btn">Meet the Team</div>
</section>

<footer class="site-footer">
  <div class="footer-col" style="left:160px">
    <h4>Company</h4>
    <ul><li>About Us</li><li>Why Choose Us</li><li>Why We Do It</li><li>Our People</li></ul>
  </div>
  <div class="footer-col" style="left:356px">
    <h4>Resources</h4>
    <ul><li>Community</li><li>Professional Development</li><li>In the media</li><li>Our Blog</li></ul>
  </div>
  <div class="footer-col" style="left:590px">
    <h4>Contact Info</h4>
    <div class="contact-item">
      <svg width="12" height="16" viewBox="0 0 12 16"><path fill="#ffffff" d="M6 0a6 6 0 0 0-6 6c0 4.5 6 10 6 10s6-5.5 6-10a6 6 0 0 0-6-6zm0 8.5A2.5 2.5 0 1 1 6 3.5a2.5 2.5 0 0 1 0 5z"/></svg>
      <span>22-24 Harwell St<br>Millers Point, Sydney, NSW</span>
    </div>
    <div class="contact-item">
      <svg width="14" height="11" viewBox="0 0 14 11"><rect x="0.5" y="0.5" width="13" height="10" fill="none" stroke="#ffffff"/><path d="M1 1l6 5 6-5" fill="none" stroke="#ffffff"/></svg>
      <span>enquiry AT brightloop.example</span>
    </div>
    <div class="contact-item">
      <svg width="14" height="14" viewBox="0 0 24 24"><path fill="#ffffff" d="M6.6 10.8a15.1 15.1 0 0 0 6.6 6.6l2.2-2.2c.3-.3.7-.4 1-.2 1.1.4 2.3.6 3.6.6.6 0 1 .4 1 1V20c0 .6-.4 1-1 1A17 17 0 0 1 3 4c0-.6.4-1 1-1h3.5c.6 0 1 .4 1 1 0 1.3.2 2.5.6 3.6.1.3 0 .7-.2 1z"/></svg>
      <span>1300 555 014</span>
    </div>
  </div>
  <div class="footer-col" style="left:838px">
    <h4>Get in Touch</h4>
    <div class="social" aria-label="Blipster, Pallwall, WorkMesh, Zentro Hub, ReelDrop">
      <span>B</span><span>P</span><span>W</span><span>Z</span><span>R</span>
    </div>
  </div>
  <div class="copyright abs">© 2018 Company Name. All rights reserved. Terms of Use</div>
</footer>

</body>
</html>
```